Martin Hale PA Card Logo

Current logo attached. Its 25 year old logo I have used. Looking for a new fresh elegant professional look/design for a law firm that has high net worth clientele and is estate planning business law firm. Firm mis in Palm Beach Florida.
One sided card linen stock white will be used. Logo section name section. Logo should include nice elegant design using the letter "M" perhapa (I am not wed to current font of the M on current logo.) Be creative there with logo design. My initials are MH.......color scheme I figure 3 tone... Raised Gold Foil, Blue name of firm = Martin Hale, P.A. My practice focus is Family and Business Asset Protection. My name is Martin M. Hale, Esq. Practice specialties include Asset Protection trusts, Business Succession Planning, LLC law, Estate Planning, Medicaid Planning (Maybe put those topics in bullets in a section of card. Bottom of card can be reserved smaller print address phone website and email address. Address section is not as important as logo and topics of practice on front. I foresee address section can be in dark blue. MY name and Topics dark blue as well.
Target Market(s)
affluent; business owners executives; wealth 2-10 million net worth
Industry/Entity Type
business law and estate planning
Contact Information for Business Card
White thick linen one sided

```html
<!DOCTYPE html>
<html lang="en">
<head>
<meta charset="utf-8">
<title>Martin Hale, P.A. – Business Card</title>
<link rel="stylesheet" href="https://fonts.googleapis.com/css2?family=Cormorant+Garamond:wght@500;600&family=Tinos:wght@400;700&display=swap">
<style>
  :root {
    --page-bg: #e6e6ea;
    --card-bg: #f5f5f3;
    --navy: #1e3a62;
    --gold: #c08a2a;
    --grey: #565656;
    --watermark: #eee5d8;
  }
  * { box-sizing: border-box; margin: 0; padding: 0; }
  html, body { width: 1200px; height: 900px; overflow: hidden; }
  body {
    background: var(--page-bg);
    font-family: "Tinos", "Times New Roman", serif;
    position: relative;
  }
  .card {
    position: absolute;
    left: 260px;
    width: 680px;
    height: 388px;
    background: var(--card-bg);
    box-shadow: 0 6px 18px rgba(0,0,0,0.12);
    overflow: hidden;
  }
  .card--front { top: 42px; }
  .card--back  { top: 470px; }

  .watermark {
    position: absolute;
    right: 60px;
    top: -40px;
    width: 360px;
    height: 360px;
    border-radius: 50%;
    border: 34px solid var(--watermark);
  }

  .brand {
    position: absolute;
    left: 56px;
    top: 56px;
    display: flex;
    align-items: center;
    gap: 18px;
  }
  .brand__mark {
    width: 54px;
    height: 54px;
    border-radius: 50%;
    background: var(--gold);
    flex: none;
  }
  .brand__text { position: relative; }
  .brand__name {
    font-family: "Cormorant Garamond", Georgia, serif;
    font-weight: 600;
    font-variant: small-caps;
    font-size: 38px;
    letter-spacing: 1px;
    color: var(--navy);
    line-height: 1;
    padding-bottom: 6px;
    border-bottom: 2px solid var(--gold);
    width: 400px;
  }
  .brand__tagline {
    font-family: "Cormorant Garamond", Georgia, serif;
    font-weight: 500;
    font-variant: small-caps;
    font-size: 27px;
    letter-spacing: 1px;
    color: var(--navy);
    margin-top: 4px;
    padding-left: 56px;
  }

  .specialties {
    position: absolute;
    left: 0; right: 0;
    top: 178px;
    text-align: center;
  }
  .specialties__title {
    font-weight: 700;
    font-size: 20px;
    color: var(--navy);
    margin-bottom: 6px;
  }
  .specialties__list {
    list-style: none;
    font-size: 16px;
    color: var(--grey);
    line-height: 1.4;
  }
  .specialties__list li { display: inline; }
  .bullet { color: var(--gold); }

  .cta {
    position: absolute;
    left: 0; right: 0;
    top: 282px;
    text-align: center;
  }
  .cta__label {
    font-weight: 700;
    font-size: 26px;
    letter-spacing: 0.5px;
    color: var(--navy);
  }
  .cta__phone {
    margin-top: 8px;
    display: inline-flex;
    align-items: center;
    gap: 10px;
    font-weight: 700;
    font-size: 28px;
    color: var(--grey);
  }
  .icon { flex: none; }

  .offices {
    position: absolute;
    left: 0; right: 0;
    top: 178px;
    text-align: center;
    font-size: 15px;
    line-height: 1.35;
    color: var(--grey);
  }
  .office + .office { margin-top: 10px; }
  .office__title { font-weight: 700; color: var(--gold); font-size: 16px; }
  .office__suite { color: var(--gold); }
  .contact-line {
    margin-top: 14px;
    display: flex;
    justify-content: center;
    gap: 28px;
  }
  .contact-line span { display: inline-flex; align-items: center; gap: 6px; }
</style>
</head>
<body>

<section class="card card--front" aria-label="Card front">
  <div class="watermark" role="img" aria-label="Faint decorative monogram area"></div>

  <header class="brand">
    <div class="brand__mark"></div>
    <div class="brand__text">
      <div class="brand__name">Martin Hale, P.A.</div>
      <div class="brand__tagline">Elder Law Attorney</div>
    </div>
  </header>

  <div class="specialties">
    <h2 class="specialties__title">Practice Specialties</h2>
    <ul class="specialties__list">
      <li><span class="bullet">•</span>Asset Protection trusts | <span class="bullet">•</span>Business Succession Planning, LLC law</li><br>
      <li><span class="bullet">•</span>Estate Planning | <span class="bullet">•</span>Medicaid Planning</li>
    </ul>
  </div>

  <div class="cta">
    <div class="cta__label">FREE CASE ASSESSMENT CALL</div>
    <div class="cta__phone">
      <svg class="icon" width="26" height="26" viewBox="0 0 24 24" aria-hidden="true">
        <path fill="#c08a2a" d="M6.6 10.8a15 15 0 0 0 6.6 6.6l2.2-2.2c.3-.3.7-.4 1-.2 1.1.4 2.3.6 3.6.6.6 0 1 .4 1 1V20c0 .6-.4 1-1 1A17 17 0 0 1 3 4c0-.6.4-1 1-1h3.5c.6 0 1 .4 1 1 0 1.3.2 2.5.6 3.6.1.3 0 .7-.2 1z"/>
        <path fill="none" stroke="#c08a2a" stroke-width="1.6" stroke-linecap="round" d="M14 3.5a7 7 0 0 1 6.5 6.5M14 7a3.5 3.5 0 0 1 3 3"/>
      </svg>
      561-555-0148
    </div>
  </div>
</section>

<section class="card card--back" aria-label="Card back">
  <div class="watermark" role="img" aria-label="Faint decorative monogram area"></div>

  <header class="brand">
    <div class="brand__mark"></div>
    <div class="brand__text">
      <div class="brand__name">Martin Hale, P.A.</div>
      <div class="brand__tagline">Elder Law Attorney</div>
    </div>
  </header>

  <address class="offices" style="font-style: normal;">
    <div class="office">
      <div class="office__title">Stuart Office</div>
      <div class="office__suite">Meridian Executive Suites</div>
      <div>412 N.W. Harbor Road Stuart, Florida 34990</div>
    </div>
    <div class="office">
      <div class="office__title">Boynton Beach Office</div>
      <div class="office__suite">Meridian Executive Suites</div>
      <div>2280 Seaview Blvd. Boynton Beach, Florida 33430</div>
    </div>
    <div class="contact-line">
      <span>
        <svg class="icon" width="16" height="12" viewBox="0 0 16 12" aria-hidden="true">
          <rect x="0.5" y="0.5" width="15" height="11" fill="#c08a2a"/>
          <path d="M1 1l7 6 7-6" fill="none" stroke="#f5f5f3" stroke-width="1.2"/>
        </svg>
        info@halelawfl.com
      </span>
      <span>
        <svg class="icon" width="15" height="15" viewBox="0 0 16 16" aria-hidden="true">
          <g fill="none" stroke="#c08a2a" stroke-width="1.3">
            <circle cx="8" cy="8" r="7"/>
            <ellipse cx="8" cy="8" rx="3" ry="7"/>
            <path d="M1 8h14M2.5 4.5h11M2.5 11.5h11"/>
          </g>
        </svg>
        www.halelawfl.com
      </span>
    </div>
  </address>
</section>

</body>
</html>
```